Business Card for Air Cargo Brokerage

Hi Artvoyant -

Please see the images attached. I need a business card with a similar image and format but modernized. Business card should be portrait and have room for a QR code.

Thanks

```html
<!DOCTYPE html>
<html lang="en">
<head>
<meta charset="utf-8">
<title>Skyward Freight Co – Business Card</title>
<link rel="stylesheet" href="https://fonts.googleapis.com/css2?family=Exo+2:wght@700&family=Lato:wght@400&display=swap">
<style>
  :root {
    --canvas: #ececed;
    --card-light: #ffffff;
    --card-dark: #050708;
    --ink: #0b0b0c;
    --paper-text: #ffffff;
    --qr-outline: #b9b9bc;
  }
  * { margin: 0; padding: 0; box-sizing: border-box; }
  html, body { width: 1200px; height: 1200px; overflow: hidden; }
  body { background: var(--canvas); position: relative; font-family: "Lato", sans-serif; color: var(--ink); }

  .card { position: absolute; top: 390px; width: 240px; height: 420px; overflow: hidden; }
  .card--front { left: 330px; background: var(--card-light); }
  .card--back { left: 630px; background: var(--card-dark); }

  .brand { position: absolute; display: flex; align-items: center; gap: 7px;
           font-family: "Exo 2", sans-serif; font-weight: 700; white-space: nowrap; }
  .brand__mark { display: block; flex: none; }
  .card--front .brand { right: 16px; top: 36px; font-size: 16px; color: var(--ink); }
  .card--front .brand__mark { width: 9px; height: 9px; background: var(--ink); }
  .card--back .brand { left: 0; right: 0; top: 132px; justify-content: center; font-size: 19px; color: var(--paper-text); }
  .card--back .brand__mark { width: 12px; height: 12px; border-radius: 50%; background: var(--paper-text); }

  .corner-art { position: absolute; }
  .card--front .corner-art { right: 0; top: 84px; width: 78px; height: 110px;
                             background: linear-gradient(225deg, var(--ink) 0%, #3a3a3c 55%, var(--card-light) 100%); }
  .card--back .corner-art { left: 0; bottom: 0; width: 130px; height: 160px;
                            background: linear-gradient(45deg, var(--paper-text) 0%, #d9d9db 50%, var(--card-dark) 100%); }

  .person { position: absolute; left: 16px; top: 112px; }
  .person__name { font-family: "Exo 2", sans-serif; font-weight: 700; font-size: 16.5px; line-height: 1.15; }
  .person__role { font-size: 11.5px; line-height: 1.35; }

  .divider { position: absolute; left: 0; top: 158px; width: 28px; height: 1px; background: var(--ink); }

  .contacts { position: absolute; left: 16px; top: 170px; list-style: none; font-size: 11px; line-height: 15px; }
  .contacts li { display: flex; align-items: center; gap: 6px; white-space: nowrap; }
  .contacts svg { width: 8px; height: 8px; flex: none; }

  .qr-space { position: absolute; left: 16px; top: 244px; width: 100px; height: 100px;
              border: 1px dashed var(--qr-outline); }

  .tagline-band { position: absolute; left: 0; bottom: 0; width: 100%; height: 27px; background: var(--ink);
                  color: var(--paper-text); font-size: 9.5px; letter-spacing: 0.1px; white-space: nowrap;
                  display: flex; align-items: center; justify-content: center; text-transform: uppercase; }
</style>
</head>
<body>
  <section class="card card--front" aria-label="Business card front">
    <div class="brand"><span class="brand__mark"></span>Skyward Freight Co</div>

    <div class="corner-art" role="img" aria-label="Large aircraft silhouette decoration"></div>

    <div class="person">
      <p class="person__name">Daniel Harper</p>
      <p class="person__role">Managing Director</p>
    </div>

    <div class="divider"></div>

    <ul class="contacts">
      <li>
        <svg viewBox="0 0 10 10" aria-hidden="true"><path d="M2 0.5 L3.8 2.6 L2.9 3.7 Q4 6 6.3 7.1 L7.4 6.2 L9.5 8 L8.3 9.5 Q1.5 8.5 0.5 1.7 Z" fill="currentColor"/></svg>
        055-987 654 321
      </li>
      <li>
        <svg viewBox="0 0 10 10" aria-hidden="true"><rect x="0.5" y="2" width="9" height="6.5" fill="currentColor"/><path d="M0.8 2.3 L5 5.6 L9.2 2.3" stroke="#fff" stroke-width="1" fill="none"/></svg>
        info@skywardfreight.com
      </li>
      <li>
        <svg viewBox="0 0 10 10" aria-hidden="true"><circle cx="5" cy="5" r="4.4" fill="none" stroke="currentColor" stroke-width="1"/><ellipse cx="5" cy="5" rx="2" ry="4.4" fill="none" stroke="currentColor" stroke-width="0.8"/><path d="M0.8 5 H9.2 M1.6 2.8 H8.4 M1.6 7.2 H8.4" stroke="currentColor" stroke-width="0.7"/></svg>
        www.skywardfreight.com
      </li>
    </ul>

    <div class="qr-space" role="img" aria-label="Reserved space for QR code"></div>

    <div class="tagline-band">Solutions for Global Air Commerce</div>
  </section>

  <section class="card card--back" aria-label="Business card back">
    <div class="brand"><span class="brand__mark"></span>Skyward Freight Co</div>
    <div class="corner-art" role="img" aria-label="Large aircraft silhouette decoration"></div>
  </section>
</body>
</html>
```